Qolvar Energy Information Site Redesign

Re-vamp current site at qolvarenergy.com to include new logo, verbiage updates as needed, redesign, etc. Company overview and additional information on current QVR url.

```html
<!DOCTYPE html>
<html lang="en">
<head>
<meta charset="utf-8">
<title>QVR Energy</title>
<link href="https://fonts.googleapis.com/css2?family=Lato:ital,wght@0,400;0,700;0,900;1,400;1,700;1,900&family=Roboto:wght@400;500;700&display=swap" rel="stylesheet">
<style>
:root{
  --blue:#2a4a9b;
  --blue-dark:#1c2f6e;
  --navy:#1b2a5c;
  --green:#2e7d32;
  --green-dark:#1f5e24;
  --ink:#222;
  --muted:#666;
  --line:#d8d8d8;
  --white:#fff;
}
*{box-sizing:border-box;margin:0;padding:0}
html,body{width:1200px;height:3390px;overflow:hidden}
body{position:relative;background:var(--white);font-family:'Roboto',sans-serif;color:var(--ink)}
.abs{position:absolute}
.heading{font-family:'Lato',sans-serif;font-weight:900;font-style:italic;text-transform:uppercase;color:var(--ink)}

/* header */
.site-header{left:0;top:0;width:1200px;height:100px;background:var(--white);border-top:4px solid var(--blue)}
.brand{left:113px;top:30px;display:flex;align-items:center;gap:10px;font-family:'Roboto',sans-serif;font-weight:700;font-size:34px;color:var(--blue);letter-spacing:1px}
.brand-dot{width:14px;height:14px;border-radius:50%;background:var(--green)}
.main-nav{right:113px;top:40px;display:flex;gap:26px;font-size:15px;font-weight:500;color:#222}
.main-nav span.drop::after{content:" \25BE";font-size:11px}

/* hero */
.hero{left:0;top:100px;width:1200px;height:590px;background:linear-gradient(135deg,#8c97a6 0%,#5d6675 40%,#3b3f47 75%,#2a2c31 100%)}
.hero-title{left:0;top:270px;width:1200px;text-align:center;font-family:'Lato',sans-serif;font-weight:900;font-style:italic;font-size:62px;color:var(--white);letter-spacing:1px}
.hero-sub{left:300px;top:365px;width:600px;text-align:center;font-size:19px;line-height:27px;color:var(--white)}

.services{left:113px;top:615px;width:974px;height:153px;display:flex}
.service{flex:1;color:var(--white);display:flex;flex-direction:column;align-items:center;padding-top:18px;font-size:16px;font-weight:500;text-align:center;line-height:20px}
.service.green{background:var(--green)}
.service.blue{background:var(--blue)}
.service svg{margin-bottom:12px}

/* welcome */
.welcome-title{left:111px;top:864px;font-size:34px}
.welcome-text{left:113px;top:940px;width:520px;font-size:14.5px;line-height:25px;color:var(--muted);text-align:justify}
.btn{background:var(--green);color:var(--white);font-weight:700;font-size:15px;display:flex;align-items:center;justify-content:center;gap:8px;text-transform:uppercase}
.btn-arrow{width:14px;height:14px;border-radius:50%;background:var(--white);color:var(--green);font-size:10px;display:flex;align-items:center;justify-content:center}
.welcome-btn{left:113px;top:1114px;width:178px;height:54px}
.welcome-photo{left:671px;top:875px;width:418px;height:293px;background:linear-gradient(180deg,#3a4a6b 0%,#6b6a7a 45%,#c79a5a 70%,#4a4036 100%)}

/* testimonials */
.testimonials{left:0;top:1290px;width:1200px;height:378px;background:linear-gradient(90deg,var(--green-dark),#2f7d34 50%,var(--green-dark))}
.t-kicker{left:0;top:1355px;width:1200px;text-align:center;font-family:'Lato',sans-serif;font-style:italic;font-size:20px;color:var(--white);text-transform:uppercase}
.t-title{left:0;top:1383px;width:1200px;text-align:center;font-size:38px;color:var(--white)}
.t-arrow{top:1512px;color:rgba(255,255,255,.8);font-size:26px}
.avatar{width:114px;height:114px;border-radius:50%;border:4px solid var(--white);background:linear-gradient(180deg,#c9b7a6,#6d5a4c)}
.quote{width:300px;color:var(--white)}
.quote .name{font-weight:700;font-size:13px;text-transform:uppercase}
.quote .date{font-size:12px;margin-top:6px;opacity:.9}
.quote .body{font-style:italic;font-size:12.5px;line-height:21px;margin-top:10px;opacity:.9}

/* blog */
.blog-title{left:0;top:1760px;width:1200px;text-align:center;font-size:36px}
.post{top:1849px;width:314px;height:314px;border:1px solid var(--line);background:var(--white);padding:18px}
.post h3{font-family:'Lato',sans-serif;font-weight:700;font-size:20px;line-height:26px;color:var(--ink)}
.meta{display:flex;gap:24px;font-size:12.5px;color:var(--muted);margin-top:14px}
.meta i{display:inline-block;width:10px;height:10px;background:var(--blue);margin-right:6px;vertical-align:-1px}
.meta i.pin{border-radius:50% 50% 2px 2px}
.post-photo{position:absolute;left:4px;right:4px;bottom:4px;height:178px}
.post p{font-size:13px;line-height:22px;color:var(--muted);margin-top:18px}
.post .btn{width:124px;height:34px;font-size:12px;margin-top:16px}

/* community */
.community-bg{left:0;top:2163px;width:1200px;height:775px;background:linear-gradient(180deg,#fff 0%,#f2f4f7 60%,#e6eaef 100%)}
.count{left:0;top:2436px;width:1200px;text-align:center;font-family:'Lato',sans-serif;font-weight:900;font-style:italic;font-size:46px;color:var(--blue)}
.count-label{left:0;top:2490px;width:1200px;text-align:center;font-size:34px}
.community-text{left:213px;top:2563px;width:774px;text-align:center;font-size:12.5px;line-height:24px;color:var(--muted)}
.partner{top:2640px;width:176px;height:85px;background:var(--white);border:1px solid var(--line);display:flex;align-items:center;justify-content:center;font-weight:700;font-size:19px;color:var(--ink);gap:8px}
.partner .mark{width:14px;height:14px;background:var(--green)}
.p-arrow{top:2664px;font-size:28px;color:#555}
.join-btn{left:495px;top:2784px;width:208px;height:46px}

/* footer */
.site-footer{left:0;top:2938px;width:1200px;height:452px;background:linear-gradient(180deg,#1f3170,var(--navy))}
.f-head{top:3030px;font-weight:700;font-size:17px;color:var(--white);text-transform:uppercase;text-decoration:underline;text-underline-offset:5px}
.field{border:2px solid rgba(255,255,255,.75);color:var(--white);font-size:13px;padding:9px 12px}
.submit{left:113px;top:3218px;width:97px;height:32px;font-size:13px}
.links{left:606px;top:3078px;list-style:none;color:var(--white);font-size:13.5px;line-height:26px}
.links li::before{content:"\00BB";margin-right:16px}
.contact{left:843px;color:var(--white);font-size:13.5px;line-height:22px;display:flex;gap:14px}
.contact svg{flex:none;margin-top:2px}
.f-rule{left:113px;top:3304px;width:974px;height:1px;background:rgba(255,255,255,.35)}
.copyright{left:113px;top:3340px;font-size:14px;color:var(--white)}
.social{top:3333px;width:34px;height:34px;border-radius:50%;border:2px solid var(--white)}
</style>
</head>
<body>

<header class="abs site-header">
  <div class="abs brand"><span class="brand-dot"></span>QVR ENERGY</div>
  <nav class="abs main-nav">
    <span>HOME</span><span>WHAT WE DO</span><span class="drop">EXCHANGE SOLUTIONS</span><span>MORE</span><span class="drop">ABOUT QVR</span><span>BLOG</span>
  </nav>
</header>

<section class="abs hero" role="img" aria-label="Hands working on a calculator beside financial charts on a desk"></section>
<h1 class="abs hero-title">QVR ENERGY</h1>
<p class="abs hero-sub">QVR provides the technology to efficiently transfer information electronically &amp; access, integrate and manage data.</p>

<div class="abs services">
  <div class="service green">
    <svg width="56" height="60" viewBox="0 0 56 60" fill="none" stroke="#fff" stroke-width="2"><ellipse cx="28" cy="8" rx="20" ry="6"/><path d="M8 8v40c0 3 9 6 20 6s20-3 20-6V8"/><path d="M8 22c0 3 9 6 20 6s20-3 20-6M8 35c0 3 9 6 20 6s20-3 20-6"/></svg>
    Data Management<br>Solutions
  </div>
  <div class="service blue">
    <svg width="56" height="60" viewBox="0 0 56 60" fill="none" stroke="#fff" stroke-width="2"><rect x="10" y="4" width="36" height="52"/><path d="M16 14h24M16 22h24M16 30h24M16 38h16"/></svg>
    Well Data<br>Exchange
  </div>
  <div class="service green">
    <svg width="56" height="60" viewBox="0 0 56 60" fill="none" stroke="#fff" stroke-width="2"><rect x="4" y="4" width="22" height="30"/><rect x="30" y="26" width="22" height="30"/><path d="M30 12h14v10M40 18l4 4 4-4M26 48H12V38M8 42l4-4 4 4"/></svg>
    Partner Data<br>Exchange
  </div>
  <div class="service blue">
    <svg width="56" height="60" viewBox="0 0 56 60" fill="none" stroke="#fff" stroke-width="2"><rect x="8" y="4" width="40" height="52"/><path d="M16 20h24l-6-6M40 36H16l6 6"/></svg>
    E-Ticket<br>Exchange
  </div>
  <div class="service green">
    <svg width="56" height="60" viewBox="0 0 56 60" fill="none" stroke="#fff" stroke-width="2"><circle cx="28" cy="22" r="16"/><path d="M28 38v18M18 56h20M20 22h16M28 14v16"/></svg>
    Owner Relations<br>Services
  </div>
</div>

<h2 class="abs heading welcome-title">Welcome to QVR History</h2>
<p class="abs welcome-text">Qolvar Energy Information has been providing electronic exchange solutions for the energy industry for over 20 years. QVR utilizes proven data integration techniques to provide customers with cost effective methods to efficiently access, transform and distribute their data. Our customer list includes over 95% of the Fortune 500 energy companies.</p>
<div class="abs btn welcome-btn">Learn More <span class="btn-arrow">&#10148;</span></div>
<div class="abs welcome-photo" role="img" aria-label="Refinery storage tanks lit at dusk"></div>

<section class="abs testimonials" role="img" aria-label="Green tinted industrial plant backdrop"></section>
<p class="abs t-kicker">Testimonials</p>
<h2 class="abs heading t-title">What Our Clients Say</h2>
<span class="abs t-arrow" style="left:98px">&#8249;</span>
<span class="abs t-arrow" style="left:1090px">&#8250;</span>

<div class="abs avatar" style="left:153px;top:1471px" role="img" aria-label="Portrait of client Mira Solan"></div>
<div class="abs quote" style="left:296px;top:1478px">
  <div class="name">Mira Solan</div>
  <div class="date">Posted on 18 Oct 2018</div>
  <div class="body">At vero eos et accusamus et iusto odio dignies imos ducimus qui praesentium. At vero eos et accusamus et iusto odio...</div>
</div>
<div class="abs avatar" style="left:623px;top:1471px" role="img" aria-label="Portrait of client Dev Aranet"></div>
<div class="abs quote" style="left:766px;top:1478px">
  <div class="name">Dev Aranet</div>
  <div class="date">Posted on 18 Sep 2018</div>
  <div class="body">At vero eos et accusamus et iusto odio dignies imos ducimus qui praesentium. At vero eos et accusamus et iusto odio...</div>
</div>

<section class="abs community-bg" role="img" aria-label="Faint background of people working with documents"></section>

<h2 class="abs heading blog-title">From Blog Post</h2>

<article class="abs post" style="left:100px">
  <h3>Excepteur sint occaecat sunt cupidatat non proident.</h3>
  <div class="meta"><span><i class="pin"></i>Tomas Reld</span><span><i></i>Sep 30, 2018</span></div>
  <div class="post-photo" role="img" aria-label="Two colleagues reviewing data on a monitor" style="background:linear-gradient(135deg,#6b5448,#b89a86 50%,#3f4a5c)"></div>
</article>
<article class="abs post" style="left:443px">
  <h3>Nemo enim ipsam voluptatem quia voluptas sit odit</h3>
  <div class="meta"><span><i class="pin"></i>Tomas Reld</span><span><i></i>Sep 30, 2018</span></div>
  <p>Nam libero tempore, cum soluta nobis est eligendi optio cumque nihil impedit quo minus id quod ma ixime placeat fafsers cere possimus sed quia non numquam....</p>
  <div class="btn">Read More <span class="btn-arrow">&#10148;</span></div>
</article>
<article class="abs post" style="left:787px">
  <h3>Sed quia non numquam eius modi tempora incidunt</h3>
  <div class="meta"><span><i class="pin"></i>Tomas Reld</span><span><i></i>Sep 30, 2018</span></div>
  <div class="post-photo" role="img" aria-label="Team reviewing printed charts at a desk" style="background:linear-gradient(135deg,#d8dde3,#9aa3ad 50%,#4d5560)"></div>
</article>

<svg class="abs" style="left:0;top:2080px" width="1200" height="420" viewBox="0 2080 1200 420" fill="var(--green)">
  <polyline fill="none" stroke="var(--green)" stroke-width="2.5" points="0,2490 111,2418 219,2427 323,2382 425,2387 540,2346 723,2332 870,2251 981,2246 1037,2185 1123,2179 1200,2102"/>
  <circle cx="111" cy="2418" r="7"/><circle cx="219" cy="2427" r="7"/><circle cx="323" cy="2382" r="7"/><circle cx="425" cy="2387" r="7"/><circle cx="540" cy="2346" r="7"/><circle cx="723" cy="2332" r="7"/><circle cx="870" cy="2251" r="7"/><circle cx="981" cy="2246" r="7"/><circle cx="1037" cy="2185" r="7"/><circle cx="1123" cy="2179" r="7"/>
</svg>

<p class="abs count">300.000 +</p>
<h2 class="abs heading count-label">Community Members</h2>
<p class="abs community-text">Lorem ipsum dolor sit amet, consectetur adipisicing elit, sed do eiusmod tempor incididunt ut labore et dolore magna aliqua. Ut enim ad minim veniam, quis nostrud exercitation ullamco laboris nisi ut aliquip ex ea commodo consequat.</p>

<span class="abs p-arrow" style="left:60px">&#8249;</span>
<div class="abs partner" style="left:111px"><span class="mark"></span>Brenvale</div>
<div class="abs partner" style="left:312px"><span class="mark"></span>Ostrand</div>
<div class="abs partner" style="left:513px"><span class="mark"></span>Kelvane</div>
<div class="abs partner" style="left:712px"><span class="mark"></span>Dunmoor</div>
<div class="abs partner" style="left:911px"><span class="mark"></span>Taliro</div>
<span class="abs p-arrow" style="left:1124px">&#8250;</span>

<div class="abs btn join-btn">Join Us Now <span class="btn-arrow">&#10148;</span></div>

<footer class="abs site-footer" role="img" aria-label="Navy tinted oil pump silhouettes backdrop"></footer>
<h4 class="abs f-head" style="left:113px">Quick Contact</h4>
<div class="abs field" style="left:113px;top:3085px;width:188px;height:39px">Name</div>
<div class="abs field" style="left:319px;top:3085px;width:187px;height:39px">Email</div>
<div class="abs field" style="left:113px;top:3135px;width:393px;height:65px">Message</div>
<div class="abs btn submit">Submit</div>

<h4 class="abs f-head" style="left:606px">Quick Links</h4>
<ul class="abs links">
  <li>Home</li><li>About Us</li><li>Our Services</li><li>Exchange Solutions</li><li>Data Management</li><li>Contact Us</li>
</ul>

<h4 class="abs f-head" style="left:843px">Contact Us</h4>
<div class="abs contact" style="top:3082px">
  <svg width="14" height="18" viewBox="0 0 14 18" fill="none" stroke="#fff" stroke-width="1.6"><path d="M7 17s6-6 6-10A6 6 0 0 0 1 7c0 4 6 10 6 10z"/><circle cx="7" cy="7" r="2"/></svg>
  <span>123A, Sample Street, Sample main<br>City, New State 4567.</span>
</div>
<div class="abs contact" style="top:3160px">
  <svg width="14" height="16" viewBox="0 0 14 16" fill="none" stroke="#fff" stroke-width="1.6"><path d="M2 1h3l1 4-2 1c1 3 3 5 5 6l1-2 4 1v3c0 1-1 2-2 2C6 16 0 9 0 3c0-1 1-2 2-2z"/></svg>
  <span>(+1) 123 456 7890</span>
</div>
<div class="abs contact" style="top:3207px">
  <svg width="16" height="14" viewBox="0 0 16 14" fill="none" stroke="#fff" stroke-width="1.6"><rect x="1" y="2" width="14" height="10"/><path d="M1 2l7 6 7-6"/></svg>
  <span>supports@qolvarenergy.com</span>
</div>

<div class="abs f-rule"></div>
<p class="abs copyright">&copy; Copyright 2018 QVR Energy. All Rights Reserved &nbsp;&nbsp; | &nbsp;&nbsp; Privacy Policy</p>
<span class="abs social" style="left:919px" aria-label="Social profile"></span>
<span class="abs social" style="left:962px" aria-label="Social profile"></span>
<span class="abs social" style="left:1007px" aria-label="Social profile"></span>
<span class="abs social" style="left:1050px" aria-label="Social profile"></span>

</body>
</html>
```